Consulting company business cards

We have a base design, but would be willing to update. We have a new logo/"tag" that needs to be added. Current business card design is attached for reference into our "style."

Industry/Entity Type

Business

Contact Information for Business Card

Should contain name and title, office number, mobile number if appropriate, e-mail, website, physical address, and company logo.

Font styles to use
Other font styles liked:
• See current card design on GorvandBCard

Colors
0455a3
85acd3
aaaaaa

Requirements
Must have
• Our colors are navy blue, gray, and a lighter blue
Nice to have
• Design that I can easily drop in new names/titles as we hire employees.

```html
<!DOCTYPE html>
<html lang="en">
<head>
<meta charset="utf-8">
<title>Harlow Business Cards</title>
<link href="https://fonts.googleapis.com/css2?family=Montserrat:wght@400;500;700;800&display=swap" rel="stylesheet">
<style>
  :root {
    --backdrop: #2c2c2e;
    --card-gray: #8e8e93;
    --card-white: #ffffff;
    --navy: #0d3557;
    --sky: #2fa8df;
    --logo-blue: #7fa9cf;
    --text-gray: #8a8a8a;
    --illustration: #f4f4f4;
  }
  * { box-sizing: border-box; margin: 0; padding: 0; }
  html, body { width: 1200px; height: 900px; overflow: hidden; }
  body {
    background: var(--backdrop);
    font-family: "Montserrat", sans-serif;
    position: relative;
  }
  .card {
    position: absolute;
    width: 560px;
    height: 320px;
    border-radius: 22px;
    overflow: hidden;
  }
  .edge-band {
    position: absolute;
    left: 0; right: 0; bottom: 0;
    height: 12px;
    display: flex;
  }
  .edge-band .navy { background: var(--navy); flex: 0 0 58%; }
  .edge-band .sky { background: var(--sky); flex: 1; }

  /* front */
  .card-front { left: 90px; top: 100px; background: var(--card-gray); }
  .mascot-art {
    position: absolute;
    left: 210px; top: 70px;
    width: 140px; height: 130px;
    border-radius: 50% 46% 40% 40%;
    background: var(--illustration);
  }
  .front-url {
    position: absolute;
    left: 0; right: 0; bottom: 34px;
    text-align: center;
    color: #fff;
    font-size: 16px;
    letter-spacing: 0.5px;
  }
  .front-url b { font-weight: 700; }

  /* back */
  .card-back { left: 550px; top: 470px; background: var(--card-white); }
  .brand {
    position: absolute; left: 34px; top: 62px;
  }
  .brand-row { display: flex; align-items: center; gap: 8px; }
  .brand-name {
    font-weight: 800; font-size: 40px; color: var(--navy);
    letter-spacing: 0.5px; line-height: 1;
  }
  .brand-dot {
    width: 26px; height: 26px; border-radius: 50%; background: var(--logo-blue);
  }
  .brand-tag {
    margin-top: 5px;
    font-size: 9px; color: var(--text-gray); letter-spacing: 1.3px;
  }
  .person {
    position: absolute; right: 30px; top: 62px; text-align: right;
  }
  .person-name { font-weight: 800; font-size: 19px; color: var(--navy); letter-spacing: 0.5px; }
  .person-title { font-size: 12px; color: var(--sky); letter-spacing: 1px; margin-top: 2px; }
  .person-rule {
    position: absolute; right: 30px; top: 110px;
    width: 220px; height: 2px; background: var(--navy);
  }
  .address {
    position: absolute; right: 30px; top: 124px; text-align: right;
    font-size: 13px; color: var(--text-gray); line-height: 1.45;
  }
  .contact-rule {
    position: absolute; left: 180px; top: 206px;
    width: 260px; height: 2px; background: var(--navy);
  }
  .contacts {
    position: absolute; left: 182px; top: 216px;
    list-style: none;
    font-size: 13px; color: var(--text-gray); line-height: 1.45;
  }
  .contacts li { display: flex; align-items: center; gap: 8px; }
  .contacts svg { width: 10px; height: 10px; fill: var(--sky); flex: none; }
  .contacts b { color: var(--sky); font-weight: 700; }
</style>
</head>
<body>

<section class="card card-front">
  <div class="mascot-art" role="img" aria-label="White illustrated dog head mascot in profile"></div>
  <p class="front-url">www.<b>HARLOWTECH</b>.com</p>
  <div class="edge-band"><span class="navy"></span><span class="sky"></span></div>
</section>

<section class="card card-back">
  <div class="brand">
    <div class="brand-row">
      <span class="brand-name">HARLOW</span>
      <span class="brand-dot"></span>
    </div>
    <p class="brand-tag">A CLOUD CONSULTING COMPANY</p>
  </div>

  <div class="person">
    <p class="person-name">MAREN GORVAND</p>
    <p class="person-title">OFFICE MANAGER</p>
  </div>
  <div class="person-rule"></div>
  <p class="address">1180 w 48th st<br>riverton ohio 45002</p>

  <div class="contact-rule"></div>
  <ul class="contacts">
    <li><svg viewBox="0 0 10 10"><path d="M2 0l2 2-1 1.5c.8 1.5 2 2.7 3.5 3.5L8 6l2 2-1.5 2C4 10 0 6 0 1.5z"/></svg><span>555 014 2910</span></li>
    <li><svg viewBox="0 0 10 10"><rect x="2.5" y="0" width="5" height="10" rx="1"/></svg><span>555 014 2971</span></li>
    <li><svg viewBox="0 0 10 10"><path d="M0 2h10v6H0z M0 2l5 3.5L10 2" fill="none" stroke="#2fa8df" stroke-width="1"/></svg><span>mgorvand@harlowtech.com</span></li>
    <li><svg viewBox="0 0 10 10"><circle cx="5" cy="5" r="4.3" fill="none" stroke="#2fa8df" stroke-width="1.2"/><path d="M0.7 5h8.6M5 0.7v8.6" stroke="#2fa8df" stroke-width="1"/></svg><span>www.<b>HARLOWTECH</b>.com</span></li>
  </ul>

  <div class="edge-band"><span class="navy"></span><span class="sky"></span></div>
</section>

</body>
</html>
```